Luminously Grounded Vitality

We want to design a business card that is modern and appealing for an innovative psychedelic telemedicine company that provides at-home ketamine-assisted therapy along with wellness, longevity, and anti-aging medicines. We want to use our deep purple and white plus other colors you can find on our website. We don't have any strict brand guidelines yet so feel free to get creative. We want a very professional, but technology first modern design that will instill trust, peace, calm, but also be attractive to investors in the healthcare and SaaS space.

```html
<!DOCTYPE html>
<html lang="en">
<head>
<meta charset="utf-8">
<title>Luminously Grounded Vitality – Business Card</title>
<link rel="stylesheet" href="https://fonts.googleapis.com/css2?family=Open+Sans:wght@400;600;700&display=swap">
<style>
  :root {
    --stage: #222222;
    --purple-deep: #24143a;
    --purple-mid: #34204f;
    --purple-light: #4a2e6b;
    --pattern-tone: #3a2058;
    --lavender: #a98ad6;
    --pink: #d08ac4;
    --pink-bar: #c27db8;
    --white: #f4eefa;
  }
  * { box-sizing: border-box; margin: 0; padding: 0; }
  html, body { width: 1200px; height: 780px; overflow: hidden; }
  body {
    background: var(--stage);
    font-family: "Open Sans", Arial, sans-serif;
    position: relative;
  }
  .card {
    position: absolute;
    top: 230px;
    width: 560px;
    height: 320px;
    border-radius: 4px;
    overflow: hidden;
    box-shadow: 0 14px 30px rgba(0,0,0,.45);
  }
  /* Back side */
  .card-back { left: 30px; background: var(--purple-deep); }
  .card-back .pattern-fill {
    position: absolute; inset: 0;
    background: linear-gradient(135deg, var(--pattern-tone), var(--purple-deep) 60%, var(--pattern-tone));
  }
  .card-back .back-brand {
    position: absolute; right: 28px; bottom: 26px;
    display: flex; align-items: center; gap: 10px;
    color: var(--lavender); font-size: 16px; font-weight: 400;
  }
  .dot { width: 14px; height: 14px; border-radius: 50%; background: var(--lavender); flex: none; }

  /* Front side */
  .card-front {
    left: 610px;
    background: linear-gradient(100deg, var(--purple-light) 0%, var(--purple-mid) 28%, var(--purple-deep) 60%, var(--purple-deep) 100%);
  }
  .accent-bar {
    position: absolute; right: 0; top: 0;
    width: 14px; height: 80px; background: var(--pink-bar);
  }
  .identity { position: absolute; right: 30px; top: 18px; text-align: right; }
  .person-name { color: var(--pink); font-size: 27px; font-weight: 700; letter-spacing: .5px; }
  .person-title { color: var(--white); font-size: 13.5px; font-weight: 400; margin-top: 2px; }
  .symbol-space {
    position: absolute; right: 40px; bottom: 34px;
    width: 150px; height: 150px; border-radius: 50%;
    background: #3f2463;
  }
  .brand {
    position: absolute; left: 30px; top: 108px;
    display: flex; align-items: center; gap: 10px;
    color: var(--lavender); font-size: 19px; font-weight: 400;
  }
  .brand .dot { width: 18px; height: 18px; }
  .address {
    position: absolute; left: 30px; top: 170px;
    color: var(--white); font-size: 13px; line-height: 1.45;
  }
  .contacts { position: absolute; left: 30px; top: 222px; list-style: none; }
  .contacts li {
    display: flex; align-items: center; gap: 10px;
    color: var(--white); font-size: 14px; line-height: 24px;
  }
  .contacts svg { width: 14px; height: 14px; flex: none; }
</style>
</head>
<body>
  <section class="card card-back" aria-label="Business card back">
    <div class="pattern-fill" role="img" aria-label="Repeating brand symbol pattern in muted purple"></div>
    <div class="back-brand"><span class="dot"></span>Luminously Grounded Vitality</div>
  </section>

  <section class="card card-front" aria-label="Business card front">
    <div class="accent-bar"></div>
    <div class="identity">
      <p class="person-name">Marisol Keane, FNP-C</p>
      <p class="person-title">Co-founder, Chief Clinical Officer</p>
    </div>
    <div class="symbol-space" aria-hidden="true"></div>

    <div class="brand"><span class="dot"></span>Luminously Grounded Vitality</div>

    <p class="address">482 Alder Avenue, Suite 900,<br>Boulder, CO, United States, Colorado</p>

    <ul class="contacts">
      <li>
        <svg viewBox="0 0 24 24" aria-hidden="true"><path fill="var(--pink)" d="M6.6 10.8a15.2 15.2 0 0 0 6.6 6.6l2.2-2.2a1 1 0 0 1 1-.25 11.4 11.4 0 0 0 3.6.57 1 1 0 0 1 1 1V20a1 1 0 0 1-1 1A17 17 0 0 1 3 4a1 1 0 0 1 1-1h3.5a1 1 0 0 1 1 1c0 1.25.2 2.45.57 3.57a1 1 0 0 1-.25 1z"/></svg>
        +1 555-014-2290
      </li>
      <li>
        <svg viewBox="0 0 24 24" aria-hidden="true"><circle cx="12" cy="12" r="9" fill="none" stroke="var(--pink)" stroke-width="2"/><path d="M3 12h18M12 3c3 3 3 15 0 18M12 3c-3 3-3 15 0 18" fill="none" stroke="var(--pink)" stroke-width="1.6"/></svg>
        www.luminouslygrounded.com
      </li>
      <li>
        <svg viewBox="0 0 24 24" aria-hidden="true"><rect x="3" y="6" width="18" height="13" rx="1" fill="none" stroke="var(--pink)" stroke-width="2"/><path d="M3 7l9 7 9-7" fill="none" stroke="var(--pink)" stroke-width="2"/></svg>
        hello@luminouslygrounded.com
      </li>
    </ul>
  </section>
</body>
</html>
```